New Modern Design Responsive Website For Mining Company

Hi there, we need a new custom designed website for an Australian Mining company that has just relaunched.

We have just completed a new logo design contest so that will be included for you to look at.

There is an existing site to look at https://www.velbrostone.com/

Nothing should be assumed by this site other than that is the content we will be adding to it plus a blog as well. The current design and look is not at all what they want and hence why it should not be used as a base start for any new design.

They want a modern looking mobile friendly responsive design included website that appeals to the corporate market and stock investors.

They don't have a preference to colours used however colours that are considered more prestige / corporate / established and modern will most likely appeal. Colours like black/white, dark blue, gold , platinum etc would I think be more suitable but that is entirely up to you as they have not specified any colours at all.

The design should include mobile / tablet layout / design files.

If you have any questions, please get in touch any time. Thank you

Derek
Updates

Hi crew, Please confirm if you will included files for the mobile design as there has not been any mock ups from anyone showing the mobile version and how it would look? Thanks Derek

```html
<!DOCTYPE html>
<html lang="en">
<head>
<meta charset="utf-8">
<title>Velbro Stone — Explorer, Emergent Producer</title>
<link rel="stylesheet" href="https://fonts.googleapis.com/css2?family=Cinzel:wght@400;600&family=Montserrat:wght@300;400;500;600&display=swap">
<style>
:root{
  --ink:#050505;
  --panel:#0d0d0d;
  --rock:#1c1c1c;
  --line:#3a3a3a;
  --white:#f2f2f2;
  --grey:#9a9a9a;
  --gold:#e6e03a;
  --sans:'Montserrat',Arial,sans-serif;
  --serif:'Cinzel',Georgia,serif;
}
*{box-sizing:border-box;margin:0;padding:0}
html,body{width:1200px;height:4164px;overflow:hidden;background:var(--ink);color:var(--white);font-family:var(--sans)}
.page{position:relative;width:1200px;height:4164px}
.abs{position:absolute}
.btn{position:absolute;display:flex;align-items:center;gap:14px;border:1px solid var(--gold);color:var(--white);font-size:12px;height:30px;padding:0 16px;letter-spacing:.5px;white-space:nowrap}
.btn svg{width:22px;height:10px}
.small{font-size:11px;color:var(--grey)}

/* hero */
.hero{position:absolute;left:0;top:0;width:1200px;height:760px;background:radial-gradient(ellipse at 75% 25%,#4a4a4a 0%,#262626 35%,#0b0b0b 75%),var(--ink)}
.topbar{position:absolute;top:10px;left:80px;right:80px;display:flex;justify-content:space-between;font-size:10px;color:#cfcfcf}
.topbar .call{color:var(--gold)}
.nav{position:absolute;top:46px;left:80px;right:80px;height:40px;display:flex;align-items:center}
.logo{font-family:var(--sans);font-weight:600;font-size:20px;letter-spacing:1px;color:var(--white);display:flex;align-items:center;gap:8px}
.logo .dot{width:10px;height:10px;background:var(--gold)}
.nav ul{list-style:none;display:flex;gap:32px;margin-left:120px;font-family:var(--serif);font-size:13px}
.nav .contact{margin-left:auto;background:var(--gold);color:var(--ink);font-family:var(--serif);font-size:12px;padding:8px 12px;font-weight:600}
.hero h1{position:absolute;left:80px;top:218px;font-weight:400;font-size:44px;letter-spacing:3px}
.hero h2{position:absolute;left:80px;top:270px;font-weight:500;font-size:44px;color:var(--gold)}
.hero .code{position:absolute;left:80px;top:330px;font-size:14px;color:#ddd}
.hero .ledby{position:absolute;left:80px;top:462px;font-size:10px;color:#ccc;letter-spacing:1px}
.hero .rule{position:absolute;left:80px;right:80px;top:490px;border-top:1px solid #555}
.members{position:absolute;left:80px;top:556px;display:flex;gap:70px}
.member{display:flex;align-items:center;gap:14px}
.member .avatar{width:44px;height:44px;border-radius:50%;background:linear-gradient(#777,#444)}
.member b{display:block;font-weight:500;font-size:15px}
.member span{font-size:10px;color:var(--grey)}

/* headings */
.sect-title{position:absolute;font-size:46px;font-weight:400;line-height:1.15}
.sect-title em{font-style:normal;color:var(--gold)}
.hline{position:absolute;border-top:1px solid #bbb;width:60px}

.about-text{position:absolute;left:150px;top:1008px;width:470px;font-size:13px;line-height:1.7;color:#ddd}
.about-text p+p{margin-top:18px}
.photo{position:absolute;top:1372px;height:192px}

/* portfolio */
.portfolio{position:absolute;left:0;top:1660px;width:1200px;height:920px;background:radial-gradient(ellipse at 40% 45%,#3a3a3a 0%,#1a1a1a 40%,var(--ink) 75%)}
.project{position:absolute;left:150px;width:950px}
.project h3{font-weight:500;font-size:38px;line-height:1.2;color:var(--gold)}
.project p{margin-top:12px;font-size:13px;line-height:1.6;color:#ddd}
.divider{position:absolute;left:80px;right:80px;border-top:1px solid #444}

/* form */
.field{position:absolute;left:150px;width:570px;border-bottom:1px solid #888;height:36px;font-size:10px;color:#bbb;letter-spacing:1px}

/* footer */
.footer{position:absolute;left:0;top:3460px;width:1200px;height:704px;background:radial-gradient(ellipse at 55% 45%,#2c2c2c 0%,#141414 45%,var(--ink) 80%)}
.qfield{position:absolute;top:3648px;border-bottom:1px solid #777;height:30px;font-size:11px;color:#bbb}
.fcol{position:absolute;top:3850px;font-size:12px;line-height:30px;color:#ddd}
.fcol h4{font-family:var(--serif);color:var(--gold);font-size:13px;font-weight:600;line-height:22px;margin-bottom:4px}
.bottombar{position:absolute;left:80px;right:80px;top:4078px;display:flex;justify-content:space-between;font-size:10px;color:#ccc}
.copyright{position:absolute;left:0;right:0;top:4128px;text-align:center;font-size:11px;color:#999}
</style>
</head>
<body>
<div class="page">

  <svg width="0" height="0" style="position:absolute"><symbol id="arrow" viewBox="0 0 22 10"><path d="M0 5h20M16 1l4 4-4 4" stroke="#f2f2f2" fill="none" stroke-width="1.2"/></symbol></svg>

  <header class="hero" role="img" aria-label="Dark photograph of rock face at a mine site">
    <div class="topbar"><span>Suite 4, Level 6, 18 Harbour Lane, Sydney NSW 2000</span><span>Mon – Fri 8am – 5pm</span><span class="call">Call for a free estimate • 1300 555 0142</span></div>
    <nav class="nav">
      <div class="logo">VELBRO STONE<span class="dot"></span></div>
      <ul><li>Corporate</li><li>Governance</li><li>Investors</li><li>Portfolios ▾</li><li>Annual Reports</li></ul>
      <span class="contact">CONTACT</span>
    </nav>
    <h1>CU Ni CO FE AU</h1>
    <h2>Explorer -Emergent Producer</h2>
    <div class="code">Velbro ASX Code : VBS</div>
    <div class="ledby">LED BY</div>
    <div class="rule"></div>
    <div class="members">
      <div class="member"><div class="avatar" role="img" aria-label="Portrait of founding partner"></div><div><b>Member</b><span>Founding Partner</span></div></div>
      <div class="member"><div class="avatar" role="img" aria-label="Portrait of partner"></div><div><b>Member</b><span>Partner</span></div></div>
      <div class="member"><div class="avatar" role="img" aria-label="Portrait of partner"></div><div><b>Member</b><span>Partner</span></div></div>
    </div>
    <span class="btn" style="left:80px;top:656px">View our team <svg><use href="#arrow"/></svg></span>
  </header>

  <section class="about">
    <div class="hline" style="left:80px;top:876px"></div>
    <h2 class="sect-title" style="left:150px;top:840px">About<br><em>Our Company</em></h2>
    <div class="about-text">
      <p>Velbro Stone Ltd (company) is a public company listed on the Australian Securities Exchange (ASX). The company ASX code is VBS. The company is focused on mineral exploration and mining and in particular battery metals and gold.</p>
      <p>Our objective is to commence mining and production and deliver shareholder dividends as soon as is practicable.</p>
    </div>
    <span class="btn" style="left:150px;top:1232px">Know our team <svg><use href="#arrow"/></svg></span>
    <div class="photo" style="left:150px;width:270px;background:linear-gradient(135deg,#c9714a,#7a3a22)" role="img" aria-label="Copper wire coils"></div>
    <div class="photo" style="left:465px;width:270px;background:linear-gradient(135deg,#7c94b8,#1f2a3c)" role="img" aria-label="Nickel ore close-up"></div>
    <div class="photo" style="left:778px;width:272px;background:radial-gradient(circle,#d8b94a,#2a230f)" role="img" aria-label="Gold nuggets"></div>
  </section>

  <section class="portfolio" role="img" aria-label="Faded photograph of mining machinery">
    <div class="hline" style="left:1060px;top:100px"></div>
    <h2 class="sect-title" style="right:160px;top:66px;text-align:right">Our<br><em>Portfolio</em></h2>
    <div class="project" style="top:212px"><h3>Carrabeen</h3><p>Lorem ipsum dolor sit amet, consectetur adipiscing elit, sed do eiusmod tempor incididunt ut labore et dolore magna aliqua. Lorem ipsum dolor sit amet, consectetur adipiscing elit, sed do eiusmod tempor incididunt ut labore et dolore magna aliqua.</p></div>
    <span class="btn" style="left:150px;top:368px;font-size:11px">VIEW PROJECT <svg><use href="#arrow"/></svg></span>
    <div class="project" style="top:452px"><h3>Mt. Orrin</h3><p>Lorem ipsum dolor sit amet, consectetur adipiscing elit, sed do eiusmod tempor incididunt ut labore et dolore magna aliqua. Lorem ipsum dolor sit amet, consectetur adipiscing elit, sed do eiusmod tempor incididunt ut labore et dolore magna aliqua.</p></div>
    <span class="btn" style="left:150px;top:616px;font-size:11px">VIEW PROJECT <svg><use href="#arrow"/></svg></span>
    <div class="project" style="top:706px"><h3>Halvard</h3><p>Lorem ipsum dolor sit amet, consectetur adipiscing elit, sed do eiusmod tempor incididunt ut labore et dolore magna aliqua. Lorem ipsum dolor sit amet, consectetur adipiscing elit, sed do eiusmod tempor incididunt ut labore et dolore magna aliqua.</p></div>
    <span class="btn" style="left:150px;top:864px;font-size:11px">VIEW PROJECT <svg><use href="#arrow"/></svg></span>
  </section>
  <div class="divider" style="top:2640px"></div>

  <section class="contact-form">
    <div class="hline" style="left:80px;top:2764px"></div>
    <h2 class="sect-title" style="left:150px;top:2730px">Get in <em>Touch</em></h2>
    <div class="field" style="top:2824px">NAME</div>
    <div class="field" style="top:2894px">CONTACT NUMBER</div>
    <div class="field" style="top:2964px">EMAIL ADDRESS</div>
    <div class="field" style="top:3034px;height:100px">MESSAGE</div>
    <span class="btn" style="left:150px;top:3268px;font-size:11px">SUBMIT INQUIRY <svg><use href="#arrow"/></svg></span>
  </section>

  <footer class="footer" role="img" aria-label="Dark photograph of open-cut mine landscape"></footer>
  <h2 class="abs" style="left:80px;top:3560px;font-size:34px;font-weight:500">Ready to work with us?</h2>
  <div class="qfield" style="left:80px;width:280px">Full Name</div>
  <div class="qfield" style="left:430px;width:280px">Email Address</div>
  <div class="qfield" style="left:800px;width:320px">Contact Number</div>
  <span class="btn" style="left:80px;top:3712px;font-size:11px">REQUEST A QUOTE <svg><use href="#arrow"/></svg></span>
  <div class="divider" style="top:3800px"></div>

  <div class="logo abs" style="left:80px;top:3850px;font-size:16px">VELBRO STONE<span class="dot" style="width:8px;height:8px"></span></div>
  <div class="fcol" style="left:295px"><h4>CORPORATE</h4>Our Team<br>About Us</div>
  <div class="fcol" style="left:450px"><h4>GOVERNANCE</h4>Notices<br>Text<br>Text</div>
  <div class="fcol" style="left:630px"><h4>INVESTORS</h4>Investors<br>Meeting Notices<br>Others</div>
  <div class="fcol" style="left:815px"><h4>PORTFOLIO</h4>Carrabeen<br>Mt. Orrin<br>Halvard</div>
  <div class="fcol" style="left:975px"><h4>ANNUAL REPORTS</h4>Latest Reports<br>Report Archive<br>Text</div>
  <div class="divider" style="top:4050px"></div>
  <div class="bottombar"><span>Suite 4, Level 6, 18 Harbour Lane, Sydney NSW 2000</span><span>Mon – Fri 8am – 5pm</span><span style="color:var(--gold)">Call for a free estimate • 1300 555 0142</span></div>
  <div class="copyright">Copyright © 2022 Velbro Stone LTD</div>
</div>
</body>
</html>
```